Business card for my company-RKV Design Studio

I do not have a logo-I like red and keeping it clean. Information that should be on the card:
Tom Brazenhall AIA
Architecture Planning Interiors
Cell Phone-614.529.4086
email-rkvplanner4@mailvane.net
www.rkvdesignstudio.net

```html
<!DOCTYPE html>
<html lang="en">
<head>
<meta charset="utf-8">
<title>RKV Design Studio – Business Card</title>
<link rel="stylesheet" href="https://fonts.googleapis.com/css2?family=Archivo:wght@700&family=Barlow+Semi+Condensed:wght@400&family=Bodoni+Moda:opsz,wght@6..96,500&family=Montserrat:wght@400&display=swap">
<style>
  :root {
    --brand-red: #e31e26;
    --brand-red-deep: #d1202c;
    --ink: #333333;
    --paper: #ffffff;
    --backdrop: #e6e6e6;
  }
  * { margin: 0; padding: 0; box-sizing: border-box; }
  html, body {
    width: 1200px;
    height: 1200px;
    overflow: hidden;
    background: var(--backdrop);
  }
  .card {
    position: absolute;
    left: 262px;
    width: 676px;
    height: 405px;
    box-shadow: 0 3px 10px rgba(0,0,0,0.18);
  }
  .card-front { top: 170px; background: var(--paper); }
  .card-back {
    top: 625px;
    background: radial-gradient(ellipse at center, var(--brand-red) 0%, var(--brand-red-deep) 75%);
    color: var(--paper);
    text-align: center;
  }

  .identity {
    position: absolute;
    right: 359px;
    top: 172px;
    text-align: right;
    white-space: nowrap;
  }
  .person-name {
    font-family: "Archivo", Arial, sans-serif;
    font-weight: 700;
    font-size: 30px;
    line-height: 1;
    color: var(--ink);
  }
  .services {
    margin-top: 10px;
    font-family: "Barlow Semi Condensed", Arial, sans-serif;
    font-size: 16px;
    color: var(--brand-red);
    line-height: 1;
  }
  .divider {
    position: absolute;
    left: 349px;
    top: 136px;
    width: 2px;
    height: 132px;
    background: var(--ink);
  }
  .contact-list {
    position: absolute;
    left: 366px;
    top: 134px;
    list-style: none;
    font-family: "Barlow Semi Condensed", Arial, sans-serif;
    font-size: 17px;
    color: var(--ink);
    line-height: 21px;
  }
  .contact-item {
    position: relative;
    padding-left: 31px;
    white-space: nowrap;
  }
  .contact-item + .contact-item { margin-top: 11px; }
  .contact-item:nth-child(4) { margin-top: 6px; }
  .contact-icon {
    position: absolute;
    left: 0;
    top: 1px;
    width: 20px;
    height: 20px;
    fill: var(--brand-red);
    stroke: var(--brand-red);
  }

  .studio-name {
    position: absolute;
    left: 0; right: 0;
    top: 162px;
    font-family: "Bodoni Moda", "Times New Roman", serif;
    font-weight: 500;
    font-size: 56px;
    line-height: 1;
    white-space: nowrap;
  }
  .studio-web {
    position: absolute;
    left: 0; right: 0;
    top: 232px;
    font-family: "Montserrat", Arial, sans-serif;
    font-size: 17px;
    letter-spacing: 0.3em;
    padding-left: 0.3em;
    line-height: 1;
  }
</style>
</head>
<body>
  <section class="card card-front">
    <div class="identity">
      <h1 class="person-name">Tom Brazenhall AIA</h1>
      <p class="services">Architecture Planning Interiors</p>
    </div>
    <div class="divider"></div>
    <ul class="contact-list">
      <li class="contact-item">
        <svg class="contact-icon" viewBox="0 0 20 20" aria-hidden="true">
          <path stroke="none" d="M10 0.5a7.5 7.5 0 0 0-7.5 7.5c0 5 7.5 12 7.5 12s7.5-7 7.5-12A7.5 7.5 0 0 0 10 0.5zm0 10.3a3 3 0 1 1 0-6 3 3 0 0 1 0 6z"/>
        </svg>
        418 Elmwood Ave. #112 Maple Harbor,<br>Ohio 4312
      </li>
      <li class="contact-item">
        <svg class="contact-icon" viewBox="0 0 20 20" aria-hidden="true">
          <rect x="4.5" y="0.8" width="11" height="18.4" rx="1.8" fill="none" stroke-width="1.6"/>
          <circle cx="10" cy="16.3" r="0.9" stroke="none"/>
        </svg>
        614.529.4086
      </li>
      <li class="contact-item">
        <svg class="contact-icon" viewBox="0 0 20 20" aria-hidden="true">
          <rect x="0.5" y="4" width="19" height="13" stroke="none"/>
          <path d="M1 4.5l9 7 9-7M1 16.5l6.5-6M19 16.5l-6.5-6" fill="none" stroke="#fff" stroke-width="1.2"/>
        </svg>
        rkvplanner4@mailvane.net
      </li>
      <li class="contact-item">
        <svg class="contact-icon" viewBox="0 0 20 20" aria-hidden="true">
          <circle cx="10" cy="10" r="9" fill="none" stroke-width="1.5"/>
          <ellipse cx="10" cy="10" rx="4" ry="9" fill="none" stroke-width="1.2"/>
          <rect x="0.5" y="7.5" width="19" height="5" stroke="none"/>
        </svg>
        www.rkvdesignstudio.net
      </li>
    </ul>
  </section>

  <section class="card card-back">
    <h2 class="studio-name">RKV Design Studio</h2>
    <p class="studio-web">WWW.RKVDESIGNSTUDIO.NET</p>
  </section>
</body>
</html>
```